Business Card Design For DJ Company

I'm rebranding my wedding and event dj company. I am looking for a modern, luxury, & fun design to match my new logo and website design. Please see attached logo and new webpage design. Colors should match. Design should flow with logo and website for recognition. I want to attract young adults. I plan on printing metallic finish cards so please keep hat in mind.

Target Market(s)

Millennials

Contact Information for Business Card

Name: Dario Velloza
Company: Coral Tide Fiesta DJ
Services: DJ – Photo Booth – Event Lighting – LED Robot

Website: www.coraltidefiestadj.example
Email: dario@coraltidefiestadj.example
Phone: (555)014-7392

Instagram: @ctfiestadj
Facebook: @ctfiestadj
Twitter - @ctfiestadj

Se Habla Español

Font styles to use
Serif
Sans Serif

Colors

Designer to choose colors to be used in the design.

Requirements
Nice to have
• Transparent Gradient background - Image related to weddings

```html
<!DOCTYPE html>
<html lang="en">
<head>
<meta charset="utf-8">
<title>Coral Tide Fiesta DJ – Business Card</title>
<link href="https://fonts.googleapis.com/css2?family=Arimo:wght@400;700&family=Orbitron:wght@600;700&display=swap" rel="stylesheet">
<style>
  :root {
    --backdrop: #2a2a2a;
    --paper: #f2f2f2;
    --orange: #f7941d;
    --blue: #29abe2;
    --green: #8dc63f;
    --ink: #555555;
    --white: #ffffff;
  }
  * { margin: 0; padding: 0; box-sizing: border-box; }
  html, body {
    width: 1200px; height: 960px; overflow: hidden;
    background: var(--backdrop);
  }
  .canvas { position: relative; width: 1200px; height: 960px; }
  .card {
    position: absolute; width: 600px; height: 342px;
    border-radius: 20px; overflow: hidden;
  }
  .card--front { left: 302px; top: 124px; background: var(--paper); }
  .card--back { left: 299px; top: 493px; background: var(--orange); }

  .brand-mark {
    position: absolute; left: 68px; top: 78px; width: 200px; height: 190px;
    display: flex; flex-direction: column; align-items: center; justify-content: center; gap: 14px;
  }
  .brand-mark__circle {
    width: 70px; height: 70px; border-radius: 50%;
    border: 7px solid var(--blue);
  }
  .brand-mark__name {
    font-family: "Orbitron", sans-serif; font-weight: 700;
    font-size: 19px; line-height: 1.2; text-align: center;
    color: var(--orange); text-transform: uppercase; letter-spacing: 1px;
  }

  .contact { position: absolute; left: 308px; top: 86px; font-family: "Arimo", sans-serif; }
  .contact__name {
    font-family: "Orbitron", sans-serif; font-weight: 700;
    font-size: 18px; color: var(--orange); letter-spacing: 1.5px;
    text-transform: uppercase; margin-bottom: 14px;
  }
  .contact__lines { list-style: none; font-size: 14.5px; line-height: 19px; color: var(--ink); }
  .social { list-style: none; margin-top: 12px; font-size: 14.5px; line-height: 20px; color: var(--ink); }
  .social li { display: flex; align-items: center; gap: 6px; }
  .social__dot {
    width: 15px; height: 15px; border-radius: 50%;
    border: 1.5px solid var(--orange); flex: none;
  }
  .waves { position: absolute; left: 0; bottom: 0; width: 600px; height: 342px; }

  .back-mark {
    position: absolute; left: 188px; top: 50px; width: 210px; height: 200px;
    border: 9px solid var(--white); border-radius: 50%;
    display: flex; align-items: center; justify-content: center;
  }
  .back-mark__name {
    font-family: "Orbitron", sans-serif; font-weight: 700;
    font-size: 20px; line-height: 1.25; text-align: center;
    color: var(--white); text-transform: uppercase; letter-spacing: 1px;
  }
  .tagline {
    position: absolute; left: 0; width: 600px; top: 268px; text-align: center;
  }
  .tagline__language {
    display: inline-block; font-family: "Orbitron", sans-serif; font-weight: 600;
    font-size: 22px; color: var(--white); letter-spacing: 1.5px;
    padding: 0 14px 3px; border-bottom: 2px solid var(--white);
  }
  .tagline__services {
    margin-top: 6px; font-family: "Arimo", sans-serif; font-weight: 700;
    font-size: 11px; color: var(--white); letter-spacing: 0.3px;
  }
</style>
</head>
<body>
<main class="canvas">
  <section class="card card--front" aria-label="Card front">
    <div class="brand-mark">
      <span class="brand-mark__circle"></span>
      <span class="brand-mark__name">Coral Tide<br>Fiesta DJ</span>
    </div>
    <div class="contact">
      <h1 class="contact__name">Dario Velloza</h1>
      <ul class="contact__lines">
        <li>(555)014-7392</li>
        <li>dario@coraltidefiestadj.example</li>
        <li>www.coraltidefiestadj.example</li>
      </ul>
      <ul class="social">
        <li><span class="social__dot"></span>@ctfiestadj</li>
        <li><span class="social__dot"></span>/ctfiestadj</li>
        <li><span class="social__dot"></span>@ctfiestadj</li>
      </ul>
    </div>
    <svg class="waves" viewBox="0 0 600 342" aria-hidden="true">
      <path fill="var(--green)" d="M0,296 C90,310 210,318 305,311 C210,322 90,324 0,318 Z"/>
      <path fill="var(--blue)" d="M295,313 C400,298 500,290 600,302 L600,318 C500,306 400,306 295,315 Z"/>
      <path fill="var(--orange)" d="M0,322 C160,338 360,312 600,322 L600,342 L0,342 Z"/>
    </svg>
  </section>

  <section class="card card--back" aria-label="Card back">
    <div class="back-mark">
      <span class="back-mark__name">Coral Tide<br>Fiesta DJ</span>
    </div>
    <div class="tagline">
      <p class="tagline__language">Se Habla Español</p>
      <p class="tagline__services">DJ | PHOTO BOOTH | EVENT LIGHTING | LED ROBOT</p>
    </div>
  </section>
</main>
</body>
</html>
```